Plover Freightworks Business Card Design

We are a trucking and warehousing company. We run freight in the US manly from the Pacific NW to TX and back up the the PNW. We also do warehousing where we store, move, and distribute freight. Looking for a clean and modern design of business card. We would like to look rich and elegant. Attached is our logo.

Industry/Entity Type

Trucking Company

Contact Information for Business Card

Looking for a clean and modern design of business card. We would like to look rich and elegant.

Font styles to use
Sans Serif

Colors

Designer to choose colors to be used in the design.

Requirements
Must have
• logo but it should not dominate the card
Should not have
• logo should not dominate the card

```html
<!DOCTYPE html>
<html lang="en">
<head>
<meta charset="utf-8">
<title>Plover Freightworks Business Card</title>
<link rel="stylesheet" href="https://fonts.googleapis.com/css2?family=Roboto:wght@400;500;700&display=swap">
<style>
  :root {
    --backdrop: #4a433d;
    --card-dark: #3b3c3f;
    --card-dark-deep: #2c2d30;
    --paper: #ffffff;
    --brand-blue: #1a78c2;
    --accent-orange: #f39a1e;
    --text-light: #f2f2f2;
  }
  * { box-sizing: border-box; margin: 0; padding: 0; }
  html, body {
    width: 1200px; height: 930px; overflow: hidden;
    background: var(--backdrop);
    font-family: "Roboto", Arial, sans-serif;
  }
  .canvas { position: relative; width: 1200px; height: 930px; }
  .card {
    position: absolute; width: 640px; height: 366px;
    border-radius: 16px; overflow: hidden;
    background: linear-gradient(135deg, var(--card-dark) 0%, var(--card-dark-deep) 100%);
    box-shadow: 0 14px 30px rgba(0,0,0,.35);
  }
  .card--back { left: 60px; top: 50px; }
  .card--front { left: 500px; top: 510px; }

  .wordmark {
    display: flex; align-items: center; gap: 12px;
    color: var(--text-light); font-weight: 700;
    letter-spacing: 2px; text-transform: uppercase;
  }
  .wordmark__dot {
    border-radius: 50%; background: var(--brand-blue); flex: none;
  }
  .card--back .wordmark {
    position: absolute; left: 0; right: 0; top: 0; bottom: 0;
    justify-content: center; font-size: 30px;
  }
  .card--back .wordmark__dot { width: 34px; height: 34px; }

  .front__panel { position: absolute; inset: 0; }
  .front__info {
    position: absolute; right: 30px; top: 26px; width: 300px;
    text-align: right; color: var(--text-light);
  }
  .card--front .wordmark {
    justify-content: flex-end; font-size: 17px; letter-spacing: 1.5px;
  }
  .card--front .wordmark__dot { width: 18px; height: 18px; }
  .person { margin-top: 34px; }
  .person__name {
    color: var(--accent-orange); font-size: 24px; font-weight: 500;
    text-transform: uppercase; letter-spacing: .5px;
  }
  .person__title { font-size: 13px; margin-top: 2px; }
  .address { margin-top: 20px; font-size: 13px; line-height: 1.45; }
  .contacts { list-style: none; margin-top: 16px; font-size: 13px; line-height: 1.6; }
  .contacts li { display: flex; justify-content: flex-end; align-items: center; gap: 8px; }
  .contacts svg { width: 11px; height: 11px; flex: none; }
  .highlight { color: var(--accent-orange); }
</style>
</head>
<body>
<main class="canvas">
  <section class="card card--back" aria-label="Card back">
    <div class="wordmark"><span class="wordmark__dot"></span>Plover Freightworks</div>
  </section>

  <section class="card card--front" aria-label="Card front">
    <svg class="front__panel" viewBox="0 0 640 366" aria-hidden="true">
      <path d="M0,0 H250 C330,70 390,210 420,366 H0 Z" fill="var(--paper)"/>
    </svg>
    <div class="front__info">
      <div class="wordmark"><span class="wordmark__dot"></span>Plover Freightworks</div>
      <div class="person">
        <p class="person__name">Daniel Reyes</p>
        <p class="person__title">Director</p>
      </div>
      <p class="address">2187 Cedar Ridge Lane<br>Fresno, CA 93701</p>
      <ul class="contacts">
        <li>555.210.4387
          <svg viewBox="0 0 12 12"><path d="M2 1h3l1 3-1.5 1a6 6 0 0 0 2.5 2.5L8 6l3 1v3a1 1 0 0 1-1 1A9 9 0 0 1 1 2a1 1 0 0 1 1-1z" fill="var(--brand-blue)"/></svg></li>
        <li>555.318.6720
          <svg viewBox="0 0 12 12"><rect x="3" y="0.5" width="6" height="11" rx="1" fill="none" stroke="var(--brand-blue)" stroke-width="1.3"/><circle cx="6" cy="9.5" r=".8" fill="var(--brand-blue)"/></svg></li>
        <li>info@ploverfreight.com
          <svg viewBox="0 0 12 12"><rect x="0.7" y="2" width="10.6" height="8" fill="none" stroke="var(--brand-blue)" stroke-width="1.2"/><path d="M1 2.5l5 4 5-4" fill="none" stroke="var(--brand-blue)" stroke-width="1.2"/></svg></li>
        <li><span>www.<span class="highlight">ploverfreight</span>.com</span>
          <svg viewBox="0 0 12 12"><circle cx="6" cy="6" r="5.3" fill="none" stroke="var(--brand-blue)" stroke-width="1.2"/><path d="M.7 6h10.6M6 .7c-2.5 3-2.5 7.6 0 10.6M6 .7c2.5 3 2.5 7.6 0 10.6" fill="none" stroke="var(--brand-blue)" stroke-width="1"/></svg></li>
      </ul>
    </div>
  </section>
</main>
</body>
</html>
```